Design a PowerPoint template for a consultancy organisation

I am after a Powerpoint template including three pages a title slide (that should have a title and subtitle), A title and content slide and a section header slide. I expect the company name and/or logo to be prominent and the colors to work well with the logo colors. I have included a copy of the logo

```html
<!DOCTYPE html>
<html lang="en">
<head>
<meta charset="utf-8">
<title>Lumen Works — Presentation Template</title>
<link href="https://fonts.googleapis.com/css2?family=Ubuntu:wght@400;500;700&family=Open+Sans:ital,wght@0,400;0,600;1,400&display=swap" rel="stylesheet">
<style>
  :root{
    --board:#321a48;
    --purple:#6b3a9a;
    --green:#8dc63f;
    --grey:#e6e4e5;
    --white:#ffffff;
    --ink:#4a4a4a;
    --muted:#8a8a8a;
    --rule:#d5d5d5;
  }
  *{margin:0;padding:0;box-sizing:border-box}
  html,body{width:800px;height:1200px;overflow:hidden}
  body{background:var(--board);position:relative;font-family:"Open Sans",Arial,sans-serif}

  .slide{position:absolute;width:366px;height:206px;overflow:hidden;background:var(--white);box-shadow:0 4px 14px rgba(0,0,0,.35)}
  .deco{position:absolute}
  .deco--white{background:var(--white)}
  .deco--green{background:var(--green)}
  .deco--purple{background:var(--purple)}
  .photo{position:absolute}

  .title{position:absolute;font-family:"Ubuntu",Arial,sans-serif;font-weight:700;white-space:nowrap}
  .brand{position:absolute;font-family:"Ubuntu",Arial,sans-serif;font-weight:500;color:var(--green);display:flex;align-items:center;gap:3px;white-space:nowrap}
  .brand .mark{background:var(--purple);display:inline-block}
  .sub{position:absolute;font-family:"Ubuntu",Arial,sans-serif;font-weight:500;color:var(--green);font-size:8px;white-space:nowrap}
  .presenter{position:absolute;font-size:6px;color:var(--white);white-space:nowrap}
  .presenter em{font-style:italic}
  .confidential{position:absolute;font-size:3.5px;letter-spacing:.2px;color:rgba(255,255,255,.35)}

  /* title slide, purple */
  .s-title-purple{left:25px;top:30px;background:var(--purple)}
  .s-title-purple .title{left:33px;top:67px;font-size:19px;line-height:25px;color:var(--white)}

  /* title slide, photo */
  .s-title-photo{left:409px;top:30px}
  .s-title-photo .title{left:21px;top:73px;font-size:19px;line-height:25px;color:var(--purple)}
  .s-title-photo .presenter,.s-title-photo .confidential{color:var(--muted)}
  .tower-purple{right:0;top:0;width:130px;height:206px;
    background:linear-gradient(160deg,#c6acd9 0%,#7d4aa8 40%,#4a2070 100%);
    clip-path:polygon(45% 0,100% 0,100% 100%,0 100%,18% 40%)}

  /* section header */
  .s-section{left:25px;top:248px;background:var(--grey)}
  .s-section .col{position:absolute;left:0;top:0;width:61px;height:206px;background:var(--white)}
  .s-section .band{position:absolute;left:0;top:70px;width:366px;height:62px;background:var(--white)}
  .s-section .title{left:95px;top:91px;font-size:15px;color:var(--purple)}
  .s-section .subtitle{position:absolute;left:95px;top:114px;font-family:"Ubuntu",Arial,sans-serif;font-size:8px;color:var(--purple)}

  /* title and content */
  .s-content{left:409px;top:248px}
  .s-content .title{left:25px;top:23px;font-weight:400;font-size:11px;color:var(--purple)}
  .s-content .subtitle{position:absolute;left:25px;top:40px;font-size:5px;line-height:7px;color:var(--ink);border-left:.6px solid var(--purple);padding-left:2px}
  .bullets{position:absolute;left:25px;top:66px;list-style:none;font-size:5.3px;color:var(--ink);line-height:8.5px}
  .bullets li{white-space:nowrap}
  .bullets li::before{content:"–";color:var(--green);margin-right:4px}
  .bullets li.l1::before{content:"•";color:var(--ink)}
  .page-no{position:absolute;right:22px;bottom:6px;font-size:3px;color:var(--muted)}

  /* thank you */
  .s-thanks{left:217px;top:467px}
  .s-thanks .rule{position:absolute;left:37px;top:95px;width:42px;height:.5px;background:var(--rule)}
  .s-thanks .title{left:36px;top:124px;font-size:33px;color:var(--purple)}
  .s-thanks .title span{color:var(--green)}
  .tower-green{right:0;top:0;width:110px;height:175px;
    background:linear-gradient(150deg,#e2efcf 0%,#a9d46b 40%,#6fa52a 100%);
    clip-path:polygon(0 0,100% 0,100% 100%)}

  /* master layout */
  .s-master{left:233px;top:837px;width:327px;height:184px;box-shadow:none}
  .ph{position:absolute;border:.6px dashed #9c9c9c}
  .ph-title{left:22px;top:20px;width:283px;height:14px;font-family:"Ubuntu",Arial,sans-serif;font-size:9.5px;line-height:13px;color:var(--purple);padding-left:1px;white-space:nowrap}
  .ph-sub{left:22px;top:36px;width:283px;height:8px;font-size:4.6px;font-weight:600;color:var(--ink);padding-left:4px;line-height:7px;border-left:1px solid var(--green)}
  .ph-body{left:22px;top:58px;width:283px;height:39px}
  .ph-body ul{list-style:none;font-size:4.6px;color:var(--ink);line-height:7.4px;padding:1px 0 0 2px}
  .ph-body li{white-space:nowrap}
  .ph-body li::before{content:"–";color:var(--green);margin-right:3px}
  .ph-body li.l1::before{content:"•";color:var(--ink)}
  .icons{position:absolute;left:115px;top:6px;display:grid;grid-template-columns:repeat(4,10px);gap:4px}
  .icons i{width:10px;height:9px;border:.6px solid #9fb3cf;background:#eef2f8;display:block}
</style>
</head>
<body>

<!-- Title slide, purple -->
<section class="slide s-title-purple">
  <div class="deco deco--white" style="left:0;top:0;width:33px;height:59px" role="img" aria-label="Puzzle piece graphic"></div>
  <div class="deco deco--green" style="left:337px;top:147px;width:29px;height:59px" role="img" aria-label="Puzzle piece graphic"></div>
  <h1 class="title">Presentation title<br>here in this format</h1>
  <p class="sub" style="left:33px;top:123px">Subtitle here</p>
  <p class="presenter" style="left:33px;top:158px"><em>Presenter Name</em> | Date</p>
  <p class="confidential" style="left:33px;top:192px">CONFIDENTIAL</p>
</section>

<!-- Title slide, photo -->
<section class="slide s-title-photo">
  <div class="photo tower-purple" role="img" aria-label="Photo of a tall glass office tower tinted purple"></div>
  <div class="brand" style="left:20px;top:36px;font-size:9px"><span class="mark" style="width:6px;height:6px"></span>Lumen Works</div>
  <h1 class="title">Presentation title<br>here in this format</h1>
  <p class="sub" style="left:21px;top:129px">Subtitle here</p>
  <p class="presenter" style="left:21px;top:161px"><em>Presenter Name</em> | Date</p>
  <p class="confidential" style="left:21px;top:192px">CONFIDENTIAL</p>
</section>

<!-- Section header -->
<section class="slide s-section">
  <div class="col"></div>
  <div class="band"></div>
  <div class="deco deco--green" style="left:0;top:70px;width:61px;height:62px" role="img" aria-label="Puzzle piece graphic"></div>
  <div class="brand" style="left:12px;top:34px;font-size:8px"><span class="mark" style="width:5px;height:5px"></span>Lumen Works</div>
  <h2 class="title">Section header title</h2>
  <p class="subtitle">Subtitle</p>
</section>

<!-- Title and content -->
<section class="slide s-content">
  <div class="deco deco--purple" style="left:0;top:0;width:14px;height:28px" role="img" aria-label="Puzzle piece graphic"></div>
  <div class="deco deco--green" style="left:352px;top:177px;width:14px;height:29px" role="img" aria-label="Puzzle piece graphic"></div>
  <h2 class="title">Slide title here in big letters</h2>
  <p class="subtitle">Subtitle here in this format</p>
  <ul class="bullets">
    <li class="l1">Bullet style level 1</li>
    <li style="padding-left:7.5px">Bullet style level 2</li>
    <li style="padding-left:15px">Bullet style level 3</li>
    <li style="padding-left:22.5px">Bullet style level 4</li>
    <li style="padding-left:30px">Bullet style level 5</li>
  </ul>
  <div class="brand" style="left:26px;top:188px;font-size:4.5px"><span class="mark" style="width:3px;height:3px"></span>Lumen Works</div>
  <span class="page-no">4</span>
</section>

<!-- Thank you -->
<section class="slide s-thanks">
  <div class="photo tower-green" role="img" aria-label="Photo of a glass office tower tinted green"></div>
  <div class="brand" style="left:37px;top:76px;font-size:8px"><span class="mark" style="width:5px;height:5px"></span>Lumen Works</div>
  <div class="rule"></div>
  <h2 class="title">Thank <span>you</span></h2>
</section>

<!-- Master layout -->
<section class="slide s-master">
  <div class="deco deco--purple" style="left:0;top:0;width:12px;height:25px" role="img" aria-label="Puzzle piece graphic"></div>
  <div class="deco deco--green" style="left:314px;top:159px;width:13px;height:25px" role="img" aria-label="Puzzle piece graphic"></div>
  <div class="ph ph-title">Click to edit Master title style</div>
  <div class="ph ph-sub">Subtitle here</div>
  <div class="ph ph-body">
    <ul>
      <li class="l1">Click to edit Master text styles</li>
      <li style="padding-left:6px">Second level</li>
      <li style="padding-left:12px">Third level</li>
      <li style="padding-left:18px">Fourth level</li>
      <li style="padding-left:24px">Fifth level</li>
    </ul>
    <div class="icons"><i></i><i></i><i></i><i></i><i></i><i></i><i></i><i></i></div>
  </div>
  <div class="brand" style="left:24px;top:167px;font-size:3.5px;gap:2px"><span class="mark" style="width:2.5px;height:2.5px"></span>Lumen Works</div>
</section>

</body>
</html>
```